Business Card for Brenwick Painting

We need a simple, yet out standing business card for our painting company.

Target Market(s)

wealthy; high-end neighborhoods, and businesses

Industry/Entity Type

Painting

Contact Information for Business Card

Name:
Dorian Vask

Email:
d.vask@brenwick-painting.example

Website:
Brenwick-painting.example

Phone Number:
(555) 412-9063

Font styles to use
Serif
Sans Serif

Requirements
Must have
• slogan "making change simple"
Should not have
• A title attached to the name on the card

```html
<!DOCTYPE html>
<html lang="en">
<head>
<meta charset="utf-8">
<title>Brenwick Painting — Business Card</title>
<link href="https://fonts.googleapis.com/css2?family=Source+Sans+3:ital,wght@0,400;0,600;1,400&display=swap" rel="stylesheet">
<style>
  :root {
    --backdrop: #9a9b9c;
    --card: #f1f1ef;
    --green-dark: #3a5110;
    --green-light: #98b238;
    --ink: #4f4f4f;
    --rule: #b8b8b8;
  }
  * { margin: 0; padding: 0; box-sizing: border-box; }
  html, body { width: 1105px; height: 1200px; overflow: hidden; }
  body {
    background: var(--backdrop);
    font-family: "Source Sans 3", sans-serif;
    position: relative;
  }
  .card {
    position: absolute;
    left: 182px;
    width: 747px;
    height: 427px;
    background: var(--card);
    overflow: hidden;
  }
  .card--front { top: 119px; }
  .card--back { top: 635px; }

  .wordmark {
    position: absolute;
    display: flex;
    align-items: center;
    gap: 16px;
    color: var(--green-dark);
    font-weight: 600;
    white-space: nowrap;
  }
  .wordmark__square {
    background: var(--green-light);
    flex: none;
  }
  .card--front .wordmark {
    left: 0; right: 0; top: 98px;
    justify-content: center;
    font-size: 50px;
  }
  .card--front .wordmark__square { width: 34px; height: 34px; }

  .identity {
    position: absolute;
    right: calc(747px - 344px);
    top: 224px;
    text-align: right;
    font-size: 19px;
    line-height: 28px;
    color: var(--ink);
    white-space: nowrap;
  }
  .identity__name {
    font-size: 26px;
    font-weight: 600;
    color: var(--green-dark);
    line-height: 32px;
  }
  .identity__slogan { color: var(--green-light); }

  .divider {
    position: absolute;
    left: 374px;
    top: 222px;
    width: 1px;
    height: 122px;
    background: var(--rule);
  }

  .contacts {
    position: absolute;
    left: 404px;
    top: 229px;
    list-style: none;
    font-size: 19px;
    line-height: 28.5px;
    color: var(--ink);
    white-space: nowrap;
  }
  .contacts li { display: flex; align-items: center; gap: 10px; }
  .contacts svg { width: 17px; height: 17px; fill: var(--green-dark); flex: none; }

  .band-line {
    position: absolute;
    left: 0; right: 0;
    top: 390px;
    height: 3px;
    background: var(--green-dark);
  }
  .band {
    position: absolute;
    left: 0; right: 0;
    top: 397px;
    height: 30px;
    background: var(--green-dark);
  }

  .card--back .wordmark {
    left: 0; right: 0; top: 178px;
    justify-content: center;
    font-size: 56px;
  }
  .card--back .wordmark__square { width: 40px; height: 40px; }
  .website {
    position: absolute;
    left: 0; right: 0;
    top: 356px;
    text-align: center;
    font-size: 19px;
    letter-spacing: 3px;
    color: var(--ink);
  }
</style>
</head>
<body>

<section class="card card--front" aria-label="Business card front">
  <div class="wordmark">
    <span class="wordmark__square"></span>
    <span class="wordmark__name">Brenwick Painting</span>
  </div>

  <div class="identity">
    <p class="identity__name">Dorian Vask</p>
    <p class="identity__slogan">making change simple</p>
    <p>1420 Larkfield Road</p>
    <p>Harlow Bay, Oregon 90210</p>
  </div>

  <div class="divider"></div>

  <ul class="contacts">
    <li>
      <svg viewBox="0 0 16 16" aria-hidden="true"><path d="M3.2 1.2l2.3 2.6-1.3 1.8c.9 2 2.2 3.3 4.2 4.2l1.8-1.3 2.6 2.3-1.4 2.4C6.8 13.4 2.6 9.2 1.2 2.6z"/></svg>
      555 412 9063
    </li>
    <li>
      <svg viewBox="0 0 16 16" aria-hidden="true"><path d="M4.5 1h7v14h-7zM5.8 2.5v9.5h4.4V2.5zM7.3 13h1.4v1H7.3z" fill-rule="evenodd"/></svg>
      555 412 9071
    </li>
    <li>
      <svg viewBox="0 0 16 16" aria-hidden="true"><path d="M4 1h8v4H4zM1 6h14v7h-3v-2H4v2H1zM5 12h6v3H5z"/></svg>
      555 412 9088
    </li>
    <li>
      <svg viewBox="0 0 16 16" aria-hidden="true"><path d="M1 3.5h14v9H1zM2 4.5l6 4.5 6-4.5v-.1H2z"/></svg>
      d.vask@brenwick-painting.example
    </li>
  </ul>

  <div class="band-line"></div>
  <div class="band"></div>
</section>

<section class="card card--back" aria-label="Business card back">
  <div class="wordmark">
    <span class="wordmark__square"></span>
    <span class="wordmark__name">Brenwick Painting</span>
  </div>
  <p class="website">www.brenwick-painting.example</p>
</section>

</body>
</html>
```